North American Image Consultant needs a process design and a method design

I am an Image/style consultant who works with business professionals in the Toronto area. My product name is called " S.H.A.R.E." I help people understand how your " Style, Habits, Attitude, Reach and Energy. I help people create a professional appearance in a business casual/digital world, from head to toe. I work with them through all 4 seasons, to achieve consistency and confidence to help them look and feel amazing, inside and out.. easily and effortlessly. My main colour is aqua blue, I don't want any neon or primary colours. I would like it to appeal to both men and women ( but mostly women)
The final design should be an easy to follow path to success with an understanding of what S.H.A.R.E will do for them.

Target Market(s)

mid level executive business professionals 38-58 yrs old they want to look and feel amazing inside and out. They want to up their game, get the promotion, nail the interview , and feel they're relevant and taken seriously in a leadership way.

Font styles to use
Serif

Colors
b7a5cd
886aae
85cae6
33a6d7
33b8a4
f04a50
00a990
e34297
85acd3

Requirements
Must have
• A classy, casual feel. A positive feel good feeling
Nice to have
• A 3 colour balance ( Not black based)
Should not have
• Too many squares
too many squiggly lines.
Not too masculine/feminine
too childish/youthful
Not office focused or bank focused

```html
<!DOCTYPE html>
<html lang="en">
<head>
<meta charset="utf-8">
<title>S.H.A.R.E – Maintaining a Professional Appearance in a Digital World</title>
<link rel="stylesheet" href="https://fonts.googleapis.com/css2?family=Baloo+2:wght@700;800&family=Arimo:wght@400;700&display=swap">
<style>
  :root {
    --aqua-deep: #30a4d7;
    --aqua-light: #86c9e6;
    --ring-grey: #e6e7e9;
    --paper: #ffffff;
    --backdrop: #eef0f3;
  }
  * { margin: 0; padding: 0; box-sizing: border-box; }
  html, body {
    width: 1200px; height: 1200px; overflow: hidden;
    background: var(--backdrop);
  }
  body { display: flex; align-items: center; justify-content: center; }
  .process-card {
    position: relative; width: 1200px; height: 848px;
    background: var(--paper); overflow: hidden;
  }
  .brand-title {
    position: absolute; top: 12px; left: 0; width: 100%;
    text-align: center; color: var(--aqua-deep);
    font: 800 66px/1 "Baloo 2", sans-serif; letter-spacing: 2px;
  }
  .subtitle-band {
    position: absolute; top: 87px; left: 0; width: 100%; height: 62px;
    background: var(--aqua-deep); color: var(--paper);
    display: flex; align-items: center; justify-content: center;
    font: 700 33px/1 "Baloo 2", sans-serif;
  }
  .footer-band {
    position: absolute; bottom: 0; left: 0; width: 100%; height: 24px;
    background: var(--aqua-deep);
  }
  .diagram { position: absolute; inset: 0; }
  .step-label { font: 700 19px "Arimo", sans-serif; fill: var(--paper); text-anchor: middle; }
  .logo-text { font: 700 18px "Arimo", sans-serif; fill: var(--aqua-deep); text-anchor: middle; }
  .step-letter { font: 800 40px "Baloo 2", sans-serif; text-anchor: middle; }
  .step-note {
    position: absolute; width: 300px; text-align: center;
    font: 400 19px/1.25 "Arimo", sans-serif; color: var(--aqua-deep);
  }
  .note-style   { left: 47px;  top: 472px; }
  .note-habits  { left: 195px; top: 678px; }
  .note-attitude{ left: 446px; top: 764px; }
  .note-reach   { left: 701px; top: 678px; }
  .note-energy  { left: 854px; top: 470px; }
</style>
</head>
<body>
<main class="process-card">
  <h1 class="brand-title">S.H.A.R.E</h1>
  <div class="subtitle-band">Maintaining a Professional Appearance in a Digital World</div>

  <svg class="diagram" width="1200" height="848" viewBox="0 0 1200 848" aria-hidden="true">
    <defs>
      <polygon id="pent-down" points="-66,-86 66,-86 91,21 0,86 -91,21"/>
      <polygon id="pent-up" points="-66,86 66,86 91,-21 0,-86 -91,-21"/>
    </defs>

    <!-- centre logo holder -->
    <g class="logo-holder" transform="translate(596,312)">
      <circle r="127" fill="var(--ring-grey)"/>
      <circle r="108" fill="var(--paper)"/>
      <circle r="104" fill="none" stroke="var(--aqua-deep)" stroke-width="4"/>
      <text class="logo-text" y="-6">COMPANY LOGO</text>
      <text class="logo-text" y="18">HERE</text>
    </g>

    <!-- Style -->
    <g class="step step-style" transform="translate(345,364)">
      <use href="#pent-down" fill="var(--aqua-deep)" stroke="var(--paper)" stroke-width="4"/>
      <g fill="var(--paper)" transform="translate(0,-18)">
        <path d="M-40,14 L-44,-20 L-24,-2 L-12,-26 L0,-4 L12,-26 L24,-2 L44,-20 L40,14 Z"/>
        <rect x="-42" y="18" width="84" height="7"/>
        <circle cx="-44" cy="-23" r="4"/><circle cx="-12" cy="-29" r="4"/>
        <circle cx="12" cy="-29" r="4"/><circle cx="44" cy="-23" r="4"/>
      </g>
      <text class="step-label" y="41">STYLE</text>
    </g>

    <!-- Habits -->
    <g class="step step-habits" transform="translate(443,506)">
      <use href="#pent-up" fill="var(--aqua-light)" stroke="var(--paper)" stroke-width="4"/>
      <g fill="var(--paper)" transform="translate(0,-30)">
        <circle cx="-20" cy="-14" r="10"/><circle cx="20" cy="-14" r="10"/>
        <path d="M-40,20 Q-40,-2 -20,-2 Q-4,-2 -4,14 Z"/>
        <path d="M40,20 Q40,-2 20,-2 Q4,-2 4,14 Z"/>
        <circle cx="0" cy="-6" r="13"/>
        <path d="M-24,26 Q-24,6 0,6 Q24,6 24,26 Z"/>
      </g>
      <text class="step-label" y="46">HABITS</text>
    </g>

    <!-- Attitude -->
    <g class="step step-attitude" transform="translate(600,551)">
      <use href="#pent-down" fill="var(--aqua-deep)" stroke="var(--paper)" stroke-width="4"/>
      <polygon fill="var(--paper)" points="6,-58 -14,-16 0,-16 -8,14 16,-28 2,-28 14,-58"/>
      <text class="step-label" y="49">ATTITUDE</text>
    </g>

    <!-- Reach -->
    <g class="step step-reach" transform="translate(758,506)">
      <use href="#pent-up" fill="var(--aqua-light)" stroke="var(--paper)" stroke-width="4"/>
      <g fill="none" stroke="var(--paper)" stroke-width="3" transform="translate(0,-30)">
        <path d="M-30,26 L-30,10 L-10,10 L-10,-6 L10,-6 L10,-22"/>
        <path d="M26,-30 L29,-22 L37,-20 L29,-18 L26,-10 L23,-18 L15,-20 L23,-22 Z"/>
      </g>
      <text class="step-label" y="46">REACH</text>
    </g>

    <!-- Energy -->
    <g class="step step-energy" transform="translate(857,364)">
      <use href="#pent-down" fill="var(--aqua-deep)" stroke="var(--paper)" stroke-width="4"/>
      <g transform="translate(0,-22)" stroke="var(--paper)" fill="none">
        <circle r="26" stroke-width="4"/>
        <path d="M0,-16 L0,0 L12,8" stroke-width="4" stroke-linecap="round"/>
      </g>
      <text class="step-label" y="41">ENERGY</text>
    </g>

    <!-- letter markers -->
    <g class="markers">
      <circle cx="197" cy="421" r="38" fill="var(--paper)" stroke="var(--aqua-deep)" stroke-width="5"/>
      <text class="step-letter" x="197" y="436" fill="var(--aqua-deep)">S</text>
      <circle cx="345" cy="621" r="38" fill="var(--paper)" stroke="var(--aqua-light)" stroke-width="5"/>
      <text class="step-letter" x="345" y="636" fill="var(--aqua-light)">H</text>
      <circle cx="596" cy="703" r="38" fill="var(--paper)" stroke="var(--aqua-deep)" stroke-width="5"/>
      <text class="step-letter" x="596" y="718" fill="var(--aqua-deep)">A</text>
      <circle cx="851" cy="621" r="38" fill="var(--paper)" stroke="var(--aqua-light)" stroke-width="5"/>
      <text class="step-letter" x="851" y="636" fill="var(--aqua-light)">R</text>
      <circle cx="1004" cy="421" r="38" fill="var(--paper)" stroke="var(--aqua-deep)" stroke-width="5"/>
      <text class="step-letter" x="1004" y="436" fill="var(--aqua-deep)">E</text>
    </g>
  </svg>

  <p class="step-note note-style">Recognizing<br>your level<br>of authority</p>
  <p class="step-note note-habits">How it influences<br>your message</p>
  <p class="step-note note-attitude">The ‘Sound’ of your presence<br>when you walk into a room</p>
  <p class="step-note note-reach">Achieve consistency<br>in your apearance</p>
  <p class="step-note note-energy">Create your look<br>quickly and efficiently</p>

  <div class="footer-band"></div>
</main>
</body>
</html>
```